Brackenridge Strength Studio Chronic Pain Flyer

Double sided DL flyer required to promote a strength training studio to sufferers of chronic pain. Flyer will be displayed in osteopathy, chiropractic and massage clinics. Flyer should be clean, professional and appeal to an older (40+) demographic.

Target Market(s)

Chronic pain sufferers. Age 40+

Industry/Entity Type

Health And Wellness

Colors

Designer to choose colors to be used in the design.

Requirements
Must have
• See attached files for text copy and logo. Image(s) of people strength training with a coach or personal trainer, as well as images depicting pain in common parts of the body (such as those pictured in the supplied mock up)
• website address: brackenridgestrengthstudio.example.com.au
• phone number : 0452 918 304
• Street address: 4/63 Juniper Hollow Rd, Brackenridge
Nice to have
• Images such as in the attached files.

```html
<!DOCTYPE html>
<html lang="en">
<head>
<meta charset="utf-8">
<title>Brackenridge Strength Studio – Chronic Pain Flyer</title>
<link href="https://fonts.googleapis.com/css2?family=Montserrat:wght@400;500;600;700;800&display=swap" rel="stylesheet">
<style>
  :root {
    --bg: #9a9a9a;
    --paper: #ffffff;
    --red: #d9232d;
    --red-dark: #a5151c;
    --charcoal: #58595b;
    --grey: #8c8d8f;
    --grey-light: #c9cacc;
    --ink: #3d3e40;
  }
  * { box-sizing: border-box; margin: 0; padding: 0; }
  html, body { width: 1200px; height: 1200px; overflow: hidden; }
  body {
    background: var(--bg);
    font-family: "Montserrat", Arial, sans-serif;
    position: relative;
  }
  .flyer {
    position: absolute;
    top: 138px;
    width: 440px;
    height: 924px;
    background: var(--paper);
    overflow: hidden;
    box-shadow: 0 6px 18px rgba(0,0,0,.25);
  }
  .flyer--front { left: 120px; }
  .flyer--back { left: 640px; }

  .brand {
    position: absolute;
    left: 0; right: 0;
    display: flex;
    align-items: center;
    justify-content: center;
    gap: 10px;
  }
  .brand__mark {
    width: 26px; height: 26px;
    border-radius: 50%;
    background: var(--grey-light);
    flex: none;
  }
  .brand__name {
    font-weight: 800;
    font-size: 17px;
    letter-spacing: .5px;
    color: var(--charcoal);
    text-transform: uppercase;
  }

  .headline {
    position: absolute;
    left: 0; right: 0;
    text-align: center;
    font-weight: 800;
    line-height: 1;
  }
  .headline__lead { display: block; color: var(--charcoal); font-size: 34px; letter-spacing: -.5px; }
  .headline__main { display: block; color: var(--red); font-size: 62px; letter-spacing: -1px; margin-top: 4px; }

  .photo { position: absolute; left: 0; right: 0; }
  .photo--back-pain {
    top: 290px; height: 380px;
    background: radial-gradient(circle at 55% 62%, #e8676b 0%, #d9a4a6 16%, #bdbdbd 34%, #e2e2e2 70%, #f2f2f2 100%);
  }
  .photo--knee-pain {
    top: 0; height: 230px;
    background: radial-gradient(circle at 45% 48%, #e8676b 0%, #d8a2a4 14%, #b9b9b9 32%, #dedede 65%, #f4f4f4 100%);
  }
  .swoosh { position: absolute; left: 0; top: 0; width: 440px; height: 924px; }

  .phone {
    position: absolute;
    left: 0; right: 0;
    display: flex; align-items: center; justify-content: center; gap: 14px;
    font-weight: 700;
    font-size: 42px;
    color: var(--charcoal);
    letter-spacing: -.5px;
  }
  .icon-circle { width: 40px; height: 40px; flex: none; }

  .footer {
    position: absolute;
    left: 0; right: 0; bottom: 0;
    height: 150px;
    background: var(--charcoal);
    padding: 38px 0 0 44px;
    color: #fff;
  }
  .footer__row {
    display: flex; align-items: center; gap: 10px;
    font-size: 15px; font-weight: 500;
    margin-bottom: 14px;
    white-space: nowrap;
  }
  .footer__row svg { width: 18px; height: 18px; flex: none; }

  .tagline {
    position: absolute; left: 40px; right: 40px;
    font-size: 20px; font-weight: 600; color: var(--ink);
    text-align: center;
  }
  .body-copy {
    position: absolute; left: 40px; right: 40px;
    font-size: 13.5px; line-height: 1.45; color: var(--ink);
    text-align: justify;
  }
  .body-copy p + p { margin-top: 16px; }
</style>
</head>
<body>

<!-- Front side -->
<section class="flyer flyer--front">
  <div class="brand" style="top:62px;">
    <span class="brand__mark"></span>
    <span class="brand__name">Brackenridge Strength Studio</span>
  </div>
  <h1 class="headline" style="top:150px;">
    <span class="headline__lead">HEALTH THROUGH</span>
    <span class="headline__main">STRENGTH</span>
  </h1>

  <div class="photo photo--back-pain" role="img" aria-label="Black and white photo of a person holding their lower back, with the painful area glowing red"></div>

  <svg class="swoosh" viewBox="0 0 440 924" aria-hidden="true">
    <path d="M0,280 H440 V300 C300,300 130,330 0,420 Z" fill="#fff"/>
    <path d="M0,420 C130,330 300,300 440,300" fill="none" stroke="#58595b" stroke-width="14"/>
    <path d="M0,452 C140,352 300,322 440,318" fill="none" stroke="#d9232d" stroke-width="9"/>
    <path d="M0,468 C150,372 300,336 440,330" fill="none" stroke="#a5151c" stroke-width="4"/>
    <path d="M0,680 H440 V560 C330,650 170,668 0,650 Z" fill="#fff"/>
    <path d="M440,540 C330,632 170,650 0,632" fill="none" stroke="#d9232d" stroke-width="9"/>
    <path d="M440,562 C330,650 170,668 0,650" fill="none" stroke="#8c8d8f" stroke-width="10"/>
    <path d="M440,586 C330,672 170,690 0,676" fill="none" stroke="#58595b" stroke-width="12"/>
  </svg>

  <div class="phone" style="top:700px;">
    <svg class="icon-circle" viewBox="0 0 40 40" aria-hidden="true">
      <circle cx="20" cy="20" r="17" fill="none" stroke="#d9232d" stroke-width="3"/>
      <path d="M14 12c1-1 2-1 3 0l2 3c.6 1 .4 1.8-.4 2.4l-1 .8c.8 2 2.4 3.6 4.4 4.4l.8-1c.6-.8 1.4-1 2.4-.4l3 2c1 1 1 2 0 3l-1.2 1.2C24 29 11 16 12.8 13.2Z" fill="#d9232d"/>
    </svg>
    <span>0452 918 304</span>
  </div>

  <footer class="footer">
    <div class="footer__row">
      <svg viewBox="0 0 20 20" aria-hidden="true"><path d="M10 1a6 6 0 0 0-6 6c0 4.5 6 12 6 12s6-7.5 6-12a6 6 0 0 0-6-6Zm0 8.5A2.5 2.5 0 1 1 10 4.5a2.5 2.5 0 0 1 0 5Z" fill="#fff"/></svg>
      <span>4/63 Juniper Hollow Rd, Brackenridge</span>
    </div>
    <div class="footer__row">
      <svg viewBox="0 0 20 20" aria-hidden="true"><circle cx="10" cy="10" r="8" fill="none" stroke="#fff" stroke-width="1.6"/><path d="M2 10h16M10 2c3 3 3 13 0 16M10 2c-3 3-3 13 0 16" fill="none" stroke="#fff" stroke-width="1.4"/></svg>
      <span style="font-size:14px;">brackenridgestrengthstudio.example.com.au</span>
    </div>
  </footer>
</section>

<!-- Back side -->
<section class="flyer flyer--back">
  <div class="photo photo--knee-pain" role="img" aria-label="Black and white photo of hands holding a knee, with the painful joint glowing red"></div>

  <svg class="swoosh" viewBox="0 0 440 924" aria-hidden="true">
    <path d="M0,200 C140,250 320,230 440,120 V260 H0 Z" fill="#fff"/>
    <path d="M0,200 C140,250 320,230 440,120" fill="none" stroke="#d9232d" stroke-width="9"/>
    <path d="M0,214 C150,262 320,246 440,142" fill="none" stroke="#8c8d8f" stroke-width="9"/>
    <path d="M0,230 C150,276 320,262 440,164" fill="none" stroke="#58595b" stroke-width="11"/>
  </svg>

  <div class="brand" style="top:282px;">
    <span class="brand__mark"></span>
    <span class="brand__name">Brackenridge Strength Studio</span>
  </div>
  <h2 class="headline" style="top:340px;">
    <span class="headline__lead">HEALTH THROUGH</span>
    <span class="headline__main">STRENGTH</span>
  </h2>

  <p class="tagline" style="top:452px;">You don’t have to live in pain.</p>

  <div class="body-copy" style="top:490px;">
    <p>Strength training has been shown to improve many chronic pain conditions and is now being routinely recommended by medical and health professionals.</p>
    <p>Our private studio provides high quality strength training by expert strength coaches. We’ve helped countless people improve or eliminate chronic pain, contact us today and find out how we can help you.</p>
  </div>

  <div class="phone" style="top:700px;">
    <svg class="icon-circle" viewBox="0 0 40 40" aria-hidden="true">
      <circle cx="20" cy="20" r="17" fill="none" stroke="#d9232d" stroke-width="3"/>
      <path d="M14 12c1-1 2-1 3 0l2 3c.6 1 .4 1.8-.4 2.4l-1 .8c.8 2 2.4 3.6 4.4 4.4l.8-1c.6-.8 1.4-1 2.4-.4l3 2c1 1 1 2 0 3l-1.2 1.2C24 29 11 16 12.8 13.2Z" fill="#d9232d"/>
    </svg>
    <span>0452 918 304</span>
  </div>

  <footer class="footer">
    <div class="footer__row">
      <svg viewBox="0 0 20 20" aria-hidden="true"><path d="M10 1a6 6 0 0 0-6 6c0 4.5 6 12 6 12s6-7.5 6-12a6 6 0 0 0-6-6Zm0 8.5A2.5 2.5 0 1 1 10 4.5a2.5 2.5 0 0 1 0 5Z" fill="#fff"/></svg>
      <span>4/63 Juniper Hollow Rd, Brackenridge</span>
    </div>
    <div class="footer__row">
      <svg viewBox="0 0 20 20" aria-hidden="true"><circle cx="10" cy="10" r="8" fill="none" stroke="#fff" stroke-width="1.6"/><path d="M2 10h16M10 2c3 3 3 13 0 16M10 2c-3 3-3 13 0 16" fill="none" stroke="#fff" stroke-width="1.4"/></svg>
      <span style="font-size:14px;">brackenridgestrengthstudio.example.com.au</span>
    </div>
  </footer>
</section>

</body>
</html>
```